Alternative Health Practice - Website redesign

With regard to the welcome image, stock photos can't show the faces of other people. And please don't submit a design for a one-page website.
Hello, I am redesigning a website and need some help from a professional.
The old website is here: peter-lindqvist.net (pls note I don't want to reuse the welcome photo from the old site). Much of the written content will remain the same, so note that I also need a page layout/text colour etc that works for text heavy pages: ie www.peter-lindqvist.net/somatic-articles and www.peter-lindqvist.net/client-reviews
My effort at redesigning is underway here: https://pjlindqvist.sitebuildr.net/my-site-7
The original sitebuildr template is this one: https://www.sitebuildr.net/website-template/view/html/2868?originUrl=https%3A%2F%2Fwww.sitebuildr.net%2Fwebsite%2Ftemplates%2Fhtml%2Fhealth-wellness&tpClick=view_button&esi=6305f015-f1b5-4bdd-8dfa-47b7d756bb68
I'm pretty happy with the colour palette. My name Peter Johan Lindqvist is now the "brand" without Rooted Stillness subtitle. Regarding the Welcome section, if you are going to use my photos, it probably needs to be those two that are already there. If you want to put a stock photo there instead, that's fine.
If you want to propose something quite different to my design, I'm happy to receive design files in Photoshop or whatever and then subsequently replicate on Sitebuildr. Up to you.
Target Market(s)
Mostly women, some men ages 28-60.
Coding
Coded - Design and coding required
Number of Pages Required
5+ page
Look and feel
Each slider illustrates characteristics of the customer's brand and the style your logo design should communicate.

```html
<!DOCTYPE html>
<html lang="en">
<head>
<meta charset="utf-8">
<title>Peter Johan Lindqvist — Home</title>
<link href="https://fonts.googleapis.com/css2?family=Poppins:wght@300;400;500;600;700&display=swap" rel="stylesheet">
<style>
:root{
  --gold:#b08a3e;
  --gold-light:#d4ad5a;
  --gold-dark:#8a6828;
  --beige:#f8f2e9;
  --field:#f1e4cf;
  --ink:#1b1b1b;
  --text:#555;
  --white:#fff;
  --black:#0d0d0d;
}
*{box-sizing:border-box;margin:0;padding:0}
html,body{width:1200px;height:4769px;overflow:hidden}
body{font-family:'Poppins',sans-serif;color:var(--ink);background:var(--white);position:relative}
a{color:inherit;text-decoration:none}
.abs{position:absolute}
.btn{position:absolute;display:flex;align-items:center;justify-content:center;border-radius:20px;background:linear-gradient(90deg,var(--gold-light),var(--gold-dark));color:var(--white);font-size:14px;font-weight:500;white-space:nowrap}

/* hero */
.hero{position:absolute;left:0;top:0;width:1200px;height:676px;overflow:hidden}
.hero-photo{position:absolute;inset:0;background:linear-gradient(120deg,#7a5a4a 0%,#b89080 35%,#d9c4b8 55%,#8a6f63 80%,#5e4a42 100%)}
.hero-shade{position:absolute;inset:0;background:rgba(0,0,0,.38)}
.topbar{position:absolute;left:0;top:0;width:1200px;height:96px;background:rgba(25,23,22,.92)}
.brand{position:absolute;display:flex;align-items:center;gap:10px;color:var(--white);font-weight:500;letter-spacing:2px;font-size:17px;white-space:nowrap}
.brand-dot{width:14px;height:14px;border-radius:50%;background:var(--gold)}
.nav{position:absolute;top:40px;right:60px;display:flex;gap:34px;font-size:14px;color:var(--white);white-space:nowrap}
.nav .active{color:var(--gold-light)}
.hero-title{position:absolute;left:0;width:1200px;text-align:center;color:var(--white);top:326px;font-size:48px;font-weight:700;letter-spacing:1px;line-height:60px}
.hero-lead{position:absolute;left:290px;width:620px;top:424px;text-align:center;color:var(--white);font-size:15.5px;line-height:24px}

/* section heads */
.mark{position:absolute;left:585px;width:30px;height:30px;border-radius:50%;background:var(--gold)}
.sec-title{position:absolute;left:0;width:1200px;text-align:center;font-size:31px;font-weight:600;color:var(--ink)}

.band{position:absolute;left:0;width:1200px;background:var(--beige)}
.photo{position:absolute;border-radius:10px}

.body-text{position:absolute;font-size:12.5px;line-height:19.5px;color:var(--text)}
.body-text p{margin-bottom:10px}

/* experiences */
.exp{position:absolute;top:1413px;width:213px;text-align:center}
.exp .photo{position:relative;width:213px;height:213px;border-radius:8px}
.exp h4{margin-top:26px;color:var(--gold);font-size:15px;font-weight:600;white-space:nowrap}
.exp p{margin-top:6px;font-size:12.5px;line-height:19px;color:var(--text);padding:0 6px;height:38px;overflow:hidden}
.exp a{display:inline-block;margin-top:8px;font-size:12.5px;color:var(--ink);text-decoration:underline;font-style:italic}

/* articles */
.article{position:absolute;top:2632px;width:258px;height:313px;background:var(--white);border-radius:8px;overflow:hidden;display:block}
.article .cover{position:absolute;left:0;top:0;width:258px;height:239px}
.article .go{position:absolute;left:208px;top:221px;width:36px;height:36px;border-radius:50%;background:var(--gold);display:flex;align-items:center;justify-content:center}
.article h5{position:absolute;left:20px;top:264px;font-size:15px;font-weight:600;line-height:22px;color:var(--ink);white-space:nowrap}

/* testimonials */
.quote{position:absolute;top:3192px;width:300px}
.quote p{font-size:12.5px;line-height:21px;color:var(--text);text-align:center;height:88px}
.quote hr{border:0;border-top:1px solid #ddd;margin-top:4px}
.quote .who{display:flex;align-items:center;gap:18px;margin-top:14px}
.avatar{width:52px;height:52px;border-radius:50%;background:linear-gradient(135deg,#c9a890,#6c4f40)}
.who b{display:block;font-size:15px;font-weight:600;white-space:nowrap}
.stars{display:flex;gap:3px;margin-top:3px}
.chev{position:absolute;top:3248px}

/* contact */
.contact-box{position:absolute;left:163px;top:3597px;width:882px;height:370px;background:var(--beige);border-radius:10px}
.info{position:absolute;left:0;top:0;width:374px;height:370px;background:var(--gold);border-radius:10px;color:var(--white)}
.info h3{position:absolute;left:26px;top:38px;font-size:21px;font-weight:600}
.info-item{position:absolute;left:26px;display:flex;gap:21px}
.ic{width:36px;height:36px;border-radius:50%;border:1.5px solid var(--white);display:flex;align-items:center;justify-content:center;flex:none}
.info-item b{display:block;font-size:15px;font-weight:600}
.info-item span{display:block;font-size:12.5px;line-height:19.5px;white-space:nowrap}
.get{position:absolute;left:394px;top:38px;font-size:21px;font-weight:600;color:var(--gold)}
.field{position:absolute;height:40px;border-radius:20px;background:var(--field);color:#b9976a;font-size:12.5px;padding:12px 20px}
.field.on{background:var(--white);border:1px solid #bbb;color:var(--ink)}

.map{position:absolute;left:0;top:4045px;width:1200px;height:372px;background:linear-gradient(100deg,#e9ecec 0%,#e4eadf 45%,#dfe8e2 62%,#8fd6e8 78%,#7ed0e6 100%)}
.zoom{position:absolute;left:1104px;top:4304px;width:36px;height:72px;background:var(--white);border:1px solid #ccc;font-size:20px;color:#555;text-align:center;line-height:34px}

/* footer */
.footer{position:absolute;left:0;top:4417px;width:1200px;height:352px;background:var(--black);color:var(--white)}
.footer h6{position:absolute;top:56px;font-size:17px;font-weight:500;color:var(--gold)}
.f-links{position:absolute;left:426px;top:92px;font-size:13px;line-height:24px;display:flex;flex-direction:column}
.f-item{position:absolute;left:791px;display:flex;align-items:center;gap:14px;font-size:13px;line-height:19px;white-space:nowrap}
.f-item .ic{width:32px;height:32px;border-color:var(--gold)}
.f-rule{position:absolute;left:60px;top:306px;width:1080px;border-top:1px solid #333}
.copy{position:absolute;left:0;top:322px;width:1200px;text-align:center;font-size:12px;color:#ccc}
</style>
</head>
<body>

<!-- hero -->
<section class="hero">
  <div class="hero-photo" role="img" aria-label="Massage therapist working on a relaxed client in a treatment room"></div>
  <div class="hero-shade"></div>
  <div class="topbar"></div>
  <a class="brand" href="index.html" style="left:61px;top:36px"><span class="brand-dot"></span>PETER LINDQVIST</a>
  <nav class="nav">
    <a class="active" href="index.html">Home</a>
    <a href="the-practice.html">The Practice</a>
    <a href="about-me.html">About Me</a>
    <a href="testimonials.html">testimonial</a>
    <a href="approach.html">Approach</a>
    <a href="contact.html">Contact</a>
  </nav>
  <h1 class="hero-title">PETER LINDQVIST</h1>
  <p class="hero-lead">You may be facing physical or emotional challenges or seeking help with another aspect of your life, such as family or relationship problems.</p>
  <a class="btn" href="contact.html" style="left:520px;top:496px;width:160px;height:34px">Book A Session</a>
</section>

<!-- about -->
<div class="band" style="top:1130px;height:690px"></div>
<div class="mark" style="top:733px"></div>
<h2 class="sec-title" style="top:774px">About Us</h2>
<div class="photo" style="left:157px;top:848px;width:428px;height:378px;background:linear-gradient(135deg,#d8dde0,#8c9aa4 55%,#3e4448)" role="img" aria-label="Therapist stretching a client's leg on a treatment table"></div>
<div class="body-text" style="left:617px;top:880px;width:425px">
  <p>Growing up in Scotland I had a strong connection with nature and the outdoors. Playing outside with friends, with bikes, ball sports, and later mountaineering and rock climbing, was what most interested me.</p>
  <p>I studied at Northfield University and worked in London for a number of years as a civil servant. I subsequently set up a property business and in 2006, relocated to Spain.</p>
  <p>At thirty years of age, I found that my life had become quite compromised. I'd had a chronic low back problem since I was a teenager and was experiencing a lot of anxiety and stress, especially being around other people.</p>
</div>
<div class="abs" style="left:617px;top:1142px;color:var(--gold);font-size:17px;font-weight:500">Peter Johan Lindqvist</div>
<div class="abs" style="left:617px;top:1170px;font-size:12.5px;color:var(--text)">Rooted Stillness® Teacher</div>

<!-- experiences -->
<div class="mark" style="top:1285px"></div>
<h2 class="sec-title" style="top:1326px">Experiences</h2>
<div class="exp" style="left:83px"><div class="photo" role="img" aria-label="Portrait of a smiling woman with curly hair" style="background:linear-gradient(135deg,#6d5a40,#c59a7c)"></div><h4>Lucía Romero Vidal</h4><p>You have given me a lot of confidence in myself.</p><a href="testimonials.html">Read More</a></div>
<div class="exp" style="left:357px"><div class="photo" role="img" aria-label="Portrait of a blonde woman" style="background:linear-gradient(135deg,#2e2a26,#c9a98a)"></div><h4>Hanne Brekke</h4><p>In 20 years as a bodyworker I've never felt anything like this...</p><a href="testimonials.html">Read More</a></div>
<div class="exp" style="left:631px"><div class="photo" role="img" aria-label="Portrait of a smiling older man" style="background:linear-gradient(135deg,#8b8f94,#3b7fb8)"></div><h4>Tom Ashford</h4><p>I went to see Peter with 2 separate problems.</p><a href="testimonials.html">Read More</a></div>
<div class="exp" style="left:904px"><div class="photo" role="img" aria-label="Portrait of a smiling woman against a blue wall" style="background:linear-gradient(135deg,#2c5fb0,#d9a4b8)"></div><h4>Mireille Dufay</h4><p>I discovered Rooted Stillness 2 years ago...</p><a href="testimonials.html">Read More</a></div>

<!-- practice -->
<div class="mark" style="top:1878px"></div>
<h2 class="sec-title" style="top:1919px">The Practice</h2>
<div class="body-text" style="left:157px;top:2016px;width:420px">
  <p><span style="color:var(--ink);font-weight:500">A session typically begins by clarifying your intention or wish.</span> You may be facing physical or emotional challenges or seeking help with another aspect of your life, such as family or relationship problems.</p>
  <p>With your interest in the work clarified, I will assess how energy is flowing in your body and where there are blockages in the physical structure.</p>
  <p>Guided by your intention, I will use skills based in touch, movement and perception to facilitate greater congruence between your energy and your physical body. Via this deep listening to the body we will stimulate your natural capacity for healing and growth and you may discover something new about yourself.</p>
</div>
<a class="btn" href="the-practice.html" style="left:154px;top:2309px;width:135px;height:36px">Learn More</a>
<div class="photo" style="left:617px;top:1995px;width:426px;height:376px;background:linear-gradient(135deg,#e8e6e2,#6f86b8 55%,#2f3a55)" role="img" aria-label="Older woman exercising with dumbbells alongside a coach"></div>

<!-- articles -->
<div class="band" style="top:2448px;height:574px"></div>
<div class="mark" style="top:2507px"></div>
<h2 class="sec-title" style="top:2547px">Somatic Healing Articles</h2>
<a class="article" href="somatic-articles.html" style="left:61px"><div class="cover" role="img" aria-label="Glowing illustration of a brain inside a head" style="background:linear-gradient(135deg,#0a3f8a,#3fa6e6 60%,#e0537a)"></div><div class="go"><svg width="16" height="16" viewBox="0 0 16 16"><path d="M14 2 2 7l5 2 2 5z" fill="#fff"/></svg></div><h5>You are not your mind<br>so who's in control of you?</h5></a>
<a class="article" href="somatic-articles.html" style="left:333px"><div class="cover" role="img" aria-label="Person breaking chains against a sunset sky" style="background:linear-gradient(180deg,#3b5f80,#e08a2e 70%,#6b3a1a)"></div><div class="go"><svg width="16" height="16" viewBox="0 0 16 16"><path d="M14 2 2 7l5 2 2 5z" fill="#fff"/></svg></div><h5>Forgiveness is good<br>for you</h5></a>
<a class="article" href="somatic-articles.html" style="left:607px"><div class="cover" role="img" aria-label="Close-up of a smiling woman framed by a hand" style="background:linear-gradient(135deg,#4a3324,#b07a55 60%,#e9d3c0)"></div><div class="go"><svg width="16" height="16" viewBox="0 0 16 16"><path d="M14 2 2 7l5 2 2 5z" fill="#fff"/></svg></div><h5>Clarity: Self vs.<br>Other</h5></a>
<a class="article" href="somatic-articles.html" style="left:881px"><div class="cover" role="img" aria-label="Two babies babbling to each other" style="background:linear-gradient(135deg,#dfe8b0,#f2e6de 55%,#e3d2c2)"></div><div class="go"><svg width="16" height="16" viewBox="0 0 16 16"><path d="M14 2 2 7l5 2 2 5z" fill="#fff"/></svg></div><h5>Learning to Speak<br>Baby</h5></a>

<!-- testimonials -->
<svg width="0" height="0" style="position:absolute"><defs><path id="star" d="M7 0l2 4.6 5 .5-3.8 3.3 1.1 5L7 10.8 2.7 13.4l1.1-5L0 5.1l5-.5z"/></defs></svg>
<div class="mark" style="top:3080px"></div>
<h2 class="sec-title" style="top:3120px">Testimonial</h2>
<svg class="chev" style="left:40px" width="24" height="24" viewBox="0 0 24 24"><path d="M17 3 6 12l11 9" fill="none" stroke="#b08a3e" stroke-width="3"/></svg>
<svg class="chev" style="left:1136px" width="24" height="24" viewBox="0 0 24 24"><path d="M7 3l11 9-11 9" fill="none" stroke="#b08a3e" stroke-width="3"/></svg>
<div class="quote" style="left:93px"><p>“ My energy was low, mornings were difficult, and I carried a persistent heaviness in my chest and upper body, feeling highly alerted during the day.”</p><hr><div class="who"><div class="avatar"></div><div><b>Daria Kovalenko</b><div class="stars"><svg width="90" height="14" viewBox="0 0 90 14"><g fill="#f0b400"><use href="#star"/><use href="#star" x="18"/><use href="#star" x="36"/><use href="#star" x="54"/><use href="#star" x="72"/></g></svg></div></div></div></div>
<div class="quote" style="left:459px"><p>“ I'm not really into woo-woo stuff. And what Peter does, doesn't really make any “logical” sense. I don't know how it works, but it does.”</p><hr><div class="who"><div class="avatar"></div><div><b>Liam Hartley</b><div class="stars"><svg width="90" height="14" viewBox="0 0 90 14"><g fill="#f0b400"><use href="#star"/><use href="#star" x="18"/><use href="#star" x="36"/><use href="#star" x="54"/><use href="#star" x="72"/></g></svg></div></div></div></div>
<div class="quote" style="left:824px"><p>“ Peter is the real deal. I first saw him with a focused healing intention, but when we began working together so much more came”</p><hr><div class="who"><div class="avatar"></div><div><b>Nadia Okafor</b><div class="stars"><svg width="90" height="14" viewBox="0 0 90 14"><g fill="#f0b400"><use href="#star"/><use href="#star" x="18"/><use href="#star" x="36"/><use href="#star" x="54"/><use href="#star" x="72"/></g></svg></div></div></div></div>

<!-- contact -->
<div class="mark" style="top:3483px"></div>
<h2 class="sec-title" style="top:3523px">Contact</h2>
<div class="contact-box">
  <div class="info">
    <h3>Contact Information</h3>
    <div class="info-item" style="top:95px"><div class="ic"><svg width="14" height="18" viewBox="0 0 14 18"><path d="M7 1a6 6 0 0 0-6 6c0 4.5 6 10 6 10s6-5.5 6-10a6 6 0 0 0-6-6z" fill="none" stroke="#fff" stroke-width="1.6"/><circle cx="7" cy="7" r="2" fill="#fff"/></svg></div><div><b>Location</b><span>Rua das Oliveiras 27b</span><span>Bairro Alto Verde</span><span>Lisbon, Portugal, 1200-114</span></div></div>
    <div class="info-item" style="top:196px"><div class="ic"><svg width="16" height="16" viewBox="0 0 16 16"><path d="M3 1h3l1.5 4-2 1.2a9 9 0 0 0 4.3 4.3L11 8.5l4 1.5v3a2 2 0 0 1-2 2A13 13 0 0 1 1 3a2 2 0 0 1 2-2z" fill="none" stroke="#fff" stroke-width="1.5"/></svg></div><div><b>Telephone No</b><span>(+351) 91 204 7731</span></div></div>
    <div class="info-item" style="top:263px"><div class="ic"><svg width="16" height="12" viewBox="0 0 16 12"><rect x="1" y="1" width="14" height="10" rx="1" fill="none" stroke="#fff" stroke-width="1.5"/><path d="M1 2l7 5 7-5" fill="none" stroke="#fff" stroke-width="1.5"/></svg></div><div><b>Email</b><span>info@peter-lindqvist.net</span></div></div>
  </div>
  <div class="get">Get In Touch</div>
  <div class="field on" style="left:398px;top:85px;width:217px">First Name</div>
  <div class="field" style="left:629px;top:85px;width:217px">Last Name</div>
  <div class="field" style="left:398px;top:139px;width:217px">Email</div>
  <div class="field" style="left:629px;top:139px;width:217px">Phone No</div>
  <div class="field" style="left:398px;top:191px;width:448px;height:87px;border-radius:14px">Message</div>
  <div class="btn" style="left:398px;top:298px;width:128px;height:36px">Submit</div>
</div>

<div class="map" role="img" aria-label="Street map of Lisbon with the practice location marked"></div>
<div class="zoom">+<br>−</div>

<!-- footer -->
<footer class="footer">
  <a class="brand" href="index.html" style="left:61px;top:78px"><span class="brand-dot"></span>PETER LINDQVIST</a>
  <h6 style="left:426px">Navigation</h6>
  <nav class="f-links">
    <a href="the-practice.html">The Practice</a>
    <a href="about-me.html">About Me</a>
    <a href="testimonials.html">Testimonial</a>
    <a href="approach.html">Approach</a>
    <a href="contact.html">Contact</a>
  </nav>
  <h6 style="left:791px">Contact</h6>
  <div class="f-item" style="top:95px"><div class="ic"><svg width="14" height="14" viewBox="0 0 16 16"><path d="M3 1h3l1.5 4-2 1.2a9 9 0 0 0 4.3 4.3L11 8.5l4 1.5v3a2 2 0 0 1-2 2A13 13 0 0 1 1 3a2 2 0 0 1 2-2z" fill="none" stroke="#b08a3e" stroke-width="1.5"/></svg></div>(+351) 91 204 7731</div>
  <div class="f-item" style="top:154px"><div class="ic"><svg width="14" height="11" viewBox="0 0 16 12"><rect x="1" y="1" width="14" height="10" rx="1" fill="none" stroke="#b08a3e" stroke-width="1.5"/><path d="M1 2l7 5 7-5" fill="none" stroke="#b08a3e" stroke-width="1.5"/></svg></div>info@peter-lindqvist.net</div>
  <div class="f-item" style="top:206px;align-items:flex-start"><div class="ic"><svg width="12" height="16" viewBox="0 0 14 18"><path d="M7 1a6 6 0 0 0-6 6c0 4.5 6 10 6 10s6-5.5 6-10a6 6 0 0 0-6-6z" fill="none" stroke="#b08a3e" stroke-width="1.6"/><circle cx="7" cy="7" r="2" fill="#b08a3e"/></svg></div><div style="padding-top:8px">Rua das Oliveiras 27b<br>Bairro Alto Verde<br>Lisbon, Portugal, 1200-114.</div></div>
  <div class="f-rule"></div>
  <div class="copy">© Peter Johan Lindqvist. All Rights Reserved.</div>
</footer>

</body>
</html>
```